Medical Company in need of Modern business card design for new Wound Care clinic.

Modern business card design for our Woundcare company. Logo and description of services can be found on our website; https://www.tovrel-woundcare.com/

```html
<!DOCTYPE html>
<html lang="en">
<head>
<meta charset="utf-8">
<title>Tovrel Woundcare – Business Card</title>
<link rel="stylesheet" href="https://fonts.googleapis.com/css2?family=Montserrat:wght@400;500;700&display=swap">
<style>
  :root {
    --stage: #3b3431;
    --card: #141414;
    --gold: #c9952e;
    --gold-light: #e0ad45;
    --white: #ffffff;
    --muted: #d8d8d8;
  }
  * { margin: 0; padding: 0; box-sizing: border-box; }
  html, body {
    width: 1200px; height: 786px; overflow: hidden;
    background: var(--stage);
    font-family: "Montserrat", sans-serif;
  }
  .stage { position: relative; width: 1200px; height: 786px; }
  .card {
    position: absolute; top: 238px;
    width: 540px; height: 309px;
    background: var(--card);
    overflow: hidden;
    color: var(--white);
  }
  .card--front { left: 40px; }
  .card--back { left: 620px; }

  .brand {
    position: absolute;
    display: flex; align-items: center; gap: 10px;
    font-weight: 500; font-size: 19px; letter-spacing: 4px;
    color: var(--white); white-space: nowrap;
  }
  .brand__mark { width: 14px; height: 14px; background: var(--gold); }

  /* front */
  .card--front .brand { left: 200px; top: 70px; }
  .front__rule {
    position: absolute; left: 150px; top: 132px;
    width: 360px; height: 2px; background: var(--gold);
  }
  .person { position: absolute; left: 34px; top: 152px; }
  .person__name { font-weight: 700; font-size: 21px; color: var(--gold-light); line-height: 1.1; }
  .person__title { font-size: 12.5px; color: var(--white); margin-top: 1px; }
  .person__rule { width: 168px; height: 2px; background: var(--gold); margin-top: 10px; }

  .contacts { position: absolute; left: 38px; top: 212px; list-style: none; }
  .contacts li {
    display: flex; align-items: center; gap: 12px;
    font-size: 12.5px; color: var(--white); height: 22px;
  }
  .contacts svg { width: 12px; height: 12px; fill: var(--gold); }

  .address {
    position: absolute; right: 30px; top: 202px;
    text-align: right; font-size: 12px; line-height: 1.3; color: var(--white);
  }
  .band { position: absolute; left: 0; bottom: 0; height: 16px; }
  .band--gold { width: 72%; background: var(--gold); }
  .band--white { left: 72%; width: 28%; background: var(--white); height: 16px; top: 0; }
  .front__band-right {
    position: absolute; right: 0; bottom: 16px; width: 28%; height: 16px; background: var(--white);
  }

  /* back */
  .card--back .brand { left: 36px; top: 142px; font-size: 17px; letter-spacing: 3.5px; }
  .back__divider {
    position: absolute; left: 330px; top: 58px;
    width: 2px; height: 180px; background: var(--gold);
  }
  .services { position: absolute; left: 342px; top: 46px; width: 190px; }
  .services__title { font-weight: 700; font-size: 14.5px; color: var(--gold-light); margin-bottom: 6px; }
  .services__list { list-style: none; }
  .services__list li {
    position: relative; padding-left: 9px;
    font-size: 10.5px; line-height: 1.3; color: var(--white); margin-bottom: 2px;
  }
  .services__list li::before {
    content: ""; position: absolute; left: 0; top: 5px;
    width: 4px; height: 4px; border-radius: 50%; background: var(--gold);
  }
</style>
</head>
<body>
<main class="stage">

  <section class="card card--front" aria-label="Business card front">
    <div class="brand"><span class="brand__mark"></span>TOVREL WOUNDCARE</div>
    <div class="front__rule"></div>

    <div class="person">
      <div class="person__name">Daniel Ward</div>
      <div class="person__title">Managing Director</div>
      <div class="person__rule"></div>
    </div>

    <ul class="contacts">
      <li>
        <svg viewBox="0 0 24 24" aria-hidden="true"><path d="M6.6 10.8a15.1 15.1 0 0 0 6.6 6.6l2.2-2.2c.3-.3.7-.4 1-.2 1.1.4 2.3.6 3.6.6.6 0 1 .4 1 1V20c0 .6-.4 1-1 1A17 17 0 0 1 3 4c0-.6.4-1 1-1h3.5c.6 0 1 .4 1 1 0 1.3.2 2.5.6 3.6.1.3 0 .7-.2 1z"/></svg>
        555.014.2290
      </li>
      <li>
        <svg viewBox="0 0 24 24" aria-hidden="true"><path d="M2 5h20v14H2z M4 7v.5l8 5 8-5V7l-8 5z" fill-rule="evenodd"/></svg>
        info@tovrel-woundcare.com
      </li>
      <li>
        <svg viewBox="0 0 24 24" aria-hidden="true"><path d="M12 2a10 10 0 1 0 0 20 10 10 0 0 0 0-20zm0 2c1 1.3 1.8 3 2.1 5H9.9C10.2 7 11 5.3 12 4zM4.3 13h3.6c.1 1.5.4 2.9.9 4.1A8 8 0 0 1 4.3 13zm0-2a8 8 0 0 1 4.5-4.1c-.5 1.2-.8 2.6-.9 4.1zM12 20c-1-1.3-1.8-3-2.1-5h4.2c-.3 2-1.1 3.7-2.1 5zm-2.1-7v-2h4.2v2zm5.3 4.1c.5-1.2.8-2.6.9-4.1h3.6a8 8 0 0 1-4.5 4.1zM16.1 11c-.1-1.5-.4-2.9-.9-4.1a8 8 0 0 1 4.5 4.1z"/></svg>
        www.tovrel-woundcare.com
      </li>
    </ul>

    <address class="address" style="font-style:normal">
      42 Cedar Ridge Lane<br>Fairview, MS 39000
    </address>

    <div class="front__band-right"></div>
    <div class="band band--gold"></div>
  </section>

  <section class="card card--back" aria-label="Business card back">
    <div class="brand"><span class="brand__mark"></span>TOVREL WOUNDCARE</div>
    <div class="back__divider"></div>
    <div class="services">
      <h2 class="services__title">Our Services</h2>
      <ul class="services__list">
        <li>Hyperbaric Oxygen Therapy (HBO): A Cornerstone of Advanced Wound Care</li>
        <li>Debridement</li>
        <li>Advanced Wound Dressings</li>
        <li>Bio-engineered Skin Substitutes</li>
        <li>Compression Therapy and Edema Management</li>
      </ul>
    </div>
  </section>

</main>
</body>
</html>
```